Album art cover

Album art design concept, my band will be releasing a 11 song rock album in the next few Months. We will be using it as a CD cover, poster, online art cover, maybe even Vinyl. Working album titles are "Copper in the rain" (Preferred album title) or "A lantern under the tide". Anything abstract, painting-like design, or whatever type of design that comes to mind. Fonts are designers choice. Thank You

Target Market(s)

Music business

Colors

Designer to choose colors to be used in the design.

Requirements
Must have
• Our band logo
Nice to have
• Anything abstract, attractive painting type, maybe even some kind of a futuristic design.
Should not have
• Skulls, blood-like, scary designs, nudity, emo type of design

```html
<!DOCTYPE html>
<html lang="en">
<head>
<meta charset="utf-8">
<title>Copper in the Rain — Velvet Static</title>
<link rel="stylesheet" href="https://fonts.googleapis.com/css2?family=Michroma&family=Stardos+Stencil:wght@700&display=swap">
<style>
  :root {
    --paper: #ffffff;
    --ink: #000000;
    --paint-red: #f5101c;
    --paint-magenta: #d62fd6;
    --paint-violet: #8a3cf0;
    --paint-blue: #3a22f2;
    --paint-pale: #f3e6f7;
    --paint-rose: #f06aa8;
  }
  html, body {
    margin: 0;
    padding: 0;
    width: 1200px;
    height: 1200px;
    overflow: hidden;
    background: var(--paper);
  }
  .cover {
    position: relative;
    width: 1200px;
    height: 1200px;
    overflow: hidden;
  }
  .cover__paint {
    position: absolute;
    inset: 0;
    background:
      radial-gradient(ellipse 360px 420px at 90px 720px, var(--paint-red) 0%, rgba(245,16,28,0.55) 45%, rgba(245,16,28,0) 100%),
      radial-gradient(ellipse 420px 520px at 1130px 520px, var(--paint-blue) 0%, rgba(58,34,242,0.6) 45%, rgba(58,34,242,0) 100%),
      radial-gradient(ellipse 380px 240px at 1040px 120px, var(--paint-rose) 0%, rgba(240,106,168,0) 100%),
      radial-gradient(ellipse 520px 380px at 560px 1130px, var(--paint-magenta) 0%, rgba(214,47,214,0.5) 50%, rgba(214,47,214,0) 100%),
      radial-gradient(ellipse 520px 260px at 500px 60px, var(--paint-pale) 0%, rgba(243,230,247,0) 100%),
      linear-gradient(115deg, #f5b3c8 0%, #e25aa8 30%, #b24ee0 58%, var(--paint-violet) 78%, #6a3cf0 100%);
  }
  .cover__frame {
    position: absolute;
    left: 372px;
    top: 330px;
    width: 534px;
    height: 534px;
    border: 2.5px solid var(--ink);
  }
  .cover__panel {
    position: absolute;
    left: 395px;
    top: 354px;
    width: 493px;
    height: 492px;
    background: var(--ink);
  }
  .cover__type {
    position: absolute;
    left: 0;
    top: 0;
    width: 1200px;
    height: 1200px;
  }
  .band-name {
    font-family: "Michroma", sans-serif;
    fill: var(--paper);
    font-size: 44px;
  }
  .album-title {
    font-family: "Stardos Stencil", "Black Ops One", sans-serif;
    font-weight: 700;
    fill: var(--paper);
  }
  .album-title--main { font-size: 100px; }
  .album-title--small { font-size: 30px; }
</style>
</head>
<body>
  <main class="cover">
    <div class="cover__paint" role="img" aria-label="Abstract watercolour paint splashes in red, magenta, violet and blue with speckles and dots"></div>
    <div class="cover__frame"></div>
    <div class="cover__panel"></div>
    <svg class="cover__type" viewBox="0 0 1200 1200" xmlns="http://www.w3.org/2000/svg">
      <g class="band">
        <text class="band-name" x="818" y="490" text-anchor="end" textLength="330" lengthAdjust="spacingAndGlyphs">VELVET</text>
        <text class="band-name" x="818" y="541" text-anchor="end" textLength="300" lengthAdjust="spacingAndGlyphs">STATIC</text>
      </g>
      <g class="title">
        <text class="album-title album-title--main" x="434" y="658" textLength="416" lengthAdjust="spacingAndGlyphs">COPPER</text>
        <text class="album-title album-title--small" x="434" y="708" textLength="76" lengthAdjust="spacingAndGlyphs">IN THE</text>
        <text class="album-title album-title--main" x="520" y="726" textLength="326" lengthAdjust="spacingAndGlyphs" style="font-size:74px">RAIN</text>
      </g>
    </svg>
  </main>
</body>
</html>
```